Book Cover Design for Millennial

I need a book cover design for my book Sunward Ledger. The subtitle of the book is Seven Quiet Steps Toward Steady Ground at Work.

I'm a career coach who helps millennial career professionals. I myself am a millennial but on the older end (34). I've dealt and been through most of the challenges millennials are facing as career professionals and I wrote this book with the thought of providing guidance and aid to getting past those challenges and shedding light on fundamental habits and practices that will help them excel in their careers. In addition, the book will help them prepare millennials for our turn as the leaders, managers, etc moving forward in corporate America. The final design should have the main title of the book in it as the focal point but not the subtitle. I want the cover to communicate something NEW, Bold, Youthful, non-traditional. I want it to stick out while still maintaining a sleek and Professional look.
Updates

Hello, Designers! I want to thank you all for your submissions! The work is amazing and I greatly appreciate it. If you would I want to help out in this process by adding a few updates based on the submissions I have seen. The concept I think that is coming close to hitting the mark is Bramble Forja. What I would like to see changed about the concept is the following: Change the outfits to be more Millennial Career Professional. I have attached some ideas to the brief. I want to replace this picture with one of multiple millennials anywhere from 3 and up. I would like the pic to have diversity in it representing most races of people in the USA. I would like my name beneath sunward ledger. I'm not a known author yet so having my name that big my distract from the title of the book. Can we make the title a little bigger and so far I like the background.Thanks, DP Added Friday, September 30, 2016

Target Market(s)

Millennial Career Professionals (18 - 34 age group)

Industry/Entity Type

Life Coaching

Logo Text

Sunward Ledger

Requirements
Must have
• communicate something NEW, Bold, Youthful, non-traditional. I want it to stick out while still maintaining a sleek and Professional look.
Nice to have
• something that goes with my brand
• http://www.doranpelwick.com
Should not have
• Nothing 3D or a logo that is hard to read when placed on stationeries, business cards etc

```html
<!DOCTYPE html>
<html lang="en">
<head>
<meta charset="utf-8">
<title>Sunward Ledger — Book Cover</title>
<link rel="stylesheet" href="https://fonts.googleapis.com/css2?family=Anton&family=Bebas+Neue&family=Oswald:wght@300&family=Montserrat:wght@300;400;600&display=swap">
<style>
  :root {
    --ink: #111111;
    --night: #0a0a0c;
    --navy-top: #0b1833;
    --navy-bottom: #063c8a;
    --navy-box: #04204f;
    --navy-box-deep: #021a40;
    --frame: #3a5b93;
    --paper: #ffffff;
    --ghost: #2e2e2e;
    --ghost-sub: #3a2a12;
    --sun-core: #ef7410;
    --sun-mid: #f5ac18;
    --sun-pale: #f7ecc8;
  }
  * { margin: 0; padding: 0; box-sizing: border-box; }
  html, body { width: 1200px; height: 902px; overflow: hidden; background: #fff; }
  .cover { position: relative; width: 1200px; height: 902px; overflow: hidden; }

  /* Back cover + spine */
  .back {
    position: absolute; left: 0; top: 0; width: 614px; height: 902px;
    background: linear-gradient(180deg, var(--navy-top) 0%, #0a2456 45%, var(--navy-bottom) 100%);
  }
  .back-header {
    position: absolute; left: 0; top: 0; width: 614px; height: 124px;
    background: linear-gradient(180deg, #060606, #121212);
  }
  .back-header svg { position: absolute; left: 0; top: 0; }
  .blurb {
    position: absolute; left: 48px; top: 139px; width: 487px;
    font: 400 13.5px/17.7px "Montserrat", sans-serif; color: var(--paper);
    text-align: justify;
  }
  .author-photo {
    position: absolute; left: 47px; top: 451px; width: 163px; height: 188px;
    background: var(--navy-box); border: 1px solid var(--frame);
  }
  .about {
    position: absolute; left: 243px; top: 450px; width: 305px;
    color: var(--paper); font-family: "Montserrat", sans-serif;
  }
  .about h2 { font-weight: 600; font-size: 14px; letter-spacing: 0.2px; margin-bottom: 10px; }
  .about p { font-weight: 400; font-size: 13.5px; line-height: 17.7px; text-align: justify; }
  .publisher-block {
    position: absolute; left: 50px; top: 808px; width: 111px; height: 62px;
    background: var(--navy-box-deep);
  }
  .spine { position: absolute; left: 574px; top: 0; width: 40px; height: 902px; }

  /* Front cover */
  .front {
    position: absolute; left: 614px; top: 0; width: 586px; height: 902px;
    background:
      radial-gradient(ellipse 70% 38% at 50% 0%, var(--sun-core) 0%, rgba(239,116,16,0) 100%),
      linear-gradient(180deg, #f3a014 0%, var(--sun-mid) 28%, #f7d36c 42%, var(--sun-pale) 60%, #f3e6bf 100%);
  }
  .front-title { position: absolute; left: 0; top: 0; }
  .team-photo {
    position: absolute; left: 10px; top: 384px; width: 576px; height: 338px;
    background: linear-gradient(180deg, rgba(120,110,100,0) 0%, #6f6a66 30%, #3a3a3e 70%, #2a2a2e 100%);
    border-radius: 120px 120px 0 0 / 60px 60px 0 0;
  }
  .author-band {
    position: absolute; left: 0; top: 722px; width: 586px; height: 180px;
    background: radial-gradient(ellipse 60% 70% at 50% 45%, #2a2a2a 0%, var(--night) 100%);
  }
  .author-name {
    position: absolute; left: 50px; top: 54px;
    font: 400 72px/1 "Bebas Neue", sans-serif; color: var(--paper);
    letter-spacing: 1px; white-space: nowrap;
  }
</style>
</head>
<body>
<main class="cover">

  <section class="back">
    <div class="back-header">
      <svg width="614" height="124" viewBox="0 0 614 124">
        <text x="48" y="88" textLength="486" lengthAdjust="spacingAndGlyphs"
              font-family="Anton, sans-serif" font-size="56" fill="var(--ghost)">SUNWARD LEDGER</text>
        <text x="124" y="110" textLength="330" lengthAdjust="spacingAndGlyphs"
              font-family="Montserrat, sans-serif" font-weight="600" font-size="12" fill="var(--ghost-sub)">SEVEN QUIET STEPS TOWARD STEADY GROUND AT WORK.</text>
      </svg>
    </div>

    <p class="blurb">Lorem Ipsum is simply dummy text of the printing and typesetting industry. Lorem Ipsum has been the industry's standard dummy text ever since the 1500s, when an unknown printer took a galley of type and scrambled it to make a type specimen book. It has survived not only five centuries, but also the leap into electronic typesetting, remaining essentially unchanged. It was popularised in the 1960s with the release of Letraset sheets containing Lorem Ipsum passages, and more recently with desktop publishing software like Aldus PageMaker including versions of Lorem Ipsum. Lorem Ipsum is simply dummy text of the printing and typesetting industry. Lorem Ipsum has been the industry's standard dummy text ever since the 1500s, when an unknown printer took a galley of type and scrambled it to make a type specimen book. It has survived not only five centuries, but also the leap into electronic typesetting, remaining essentially</p>

    <div class="author-photo" role="img" aria-label="Author portrait placeholder"></div>

    <div class="about">
      <h2>ABOUT AUTHOR</h2>
      <p>Lorem Ipsum is simply dummy text of the printing and typesetting industry. Lorem Ipsum has been the industry's standard dummy text ever since the 1500s, when an unknown printer took a galley of type and scrambled it to make a type specimen book. It has survived not only five centuries, but also the leap into electronic typesetting, remaining essentially</p>
    </div>

    <div class="publisher-block"></div>

    <svg class="spine" width="40" height="902" viewBox="0 0 40 902">
      <text transform="translate(10 52) rotate(90)" x="0" y="0" textLength="392" lengthAdjust="spacingAndGlyphs"
            font-family="Montserrat, sans-serif" font-weight="300" font-size="30" fill="var(--paper)">SUNWARD LEDGER</text>
      <text transform="translate(10 572) rotate(90)" x="0" y="0" textLength="270" lengthAdjust="spacingAndGlyphs"
            font-family="Montserrat, sans-serif" font-weight="300" font-size="30" fill="var(--paper)">DORAN PELWICK</text>
    </svg>
  </section>

  <section class="front">
    <svg class="front-title" width="586" height="320" viewBox="0 0 586 320">
      <text x="52" y="136" textLength="485" lengthAdjust="spacingAndGlyphs"
            font-family="Anton, sans-serif" font-size="128" fill="var(--ink)">SUNWARD</text>
      <text x="52" y="248" textLength="485" lengthAdjust="spacingAndGlyphs"
            font-family="Anton, sans-serif" font-size="134" fill="var(--ink)">LEDGER</text>
      <text x="52" y="296" textLength="485" lengthAdjust="spacingAndGlyphs"
            font-family="Oswald, sans-serif" font-weight="300" font-size="29" fill="#2a1d0a">SEVEN QUIET STEPS TOWARD STEADY GROUND AT WORK.</text>
    </svg>

    <div class="team-photo" role="img" aria-label="Photo of a diverse group of young career professionals in business attire"></div>

    <div class="author-band">
      <div class="author-name">DORAN PELWICK</div>
    </div>
  </section>

</main>
</body>
</html>
```